Tranquil Harbour Hypnotherapy 2017 DL Card Flyer

We would like a double sided DL Card Flyer design.

We are a professional Hypnotherapy Clinic looking for a fresh clean design.

Front of card is summary info and back of flyer is detailed text.

I have attached documents with text for the front (dl size hypno 1) and back (dl size hypno 2) of the card and an indicative style of layout.

There are logo files uploaded as well as one image file.

The colors we like are blue, white and yellow/gold.
Updates

please note: when using the 'new mindset new results' image, please only use the top half of the image. The girl is not to be in the image, just the words and light bulb with the chalk underline. thanks.. Added Sunday, March 19, 2017

Industry/Entity Type

Health And Wellness

Requirements
Must have
• Note. I have misspelled the www.TranquilHarbourHypnotherapy.com.au (missing an 'o' in the attachments to the brief). My error. Please amend in your design submissions.

```html
<!DOCTYPE html>
<html lang="en">
<head>
<meta charset="utf-8">
<title>Tranquil Harbour Hypnotherapy – DL Flyer</title>
<link rel="stylesheet" href="https://fonts.googleapis.com/css2?family=Arimo:wght@400;700&family=Oswald:wght@600&display=swap">
<style>
  :root {
    --navy: #222a5e;
    --navy-deep: #1d2452;
    --white: #ffffff;
    --grey: #6d6e72;
    --grey-light: #8a8b8f;
    --ink: #1f1f1f;
    --board-dark: #2b2b2b;
    --board-mid: #4a4a4a;
    --stage: #4b4b4d;
  }
  * { margin: 0; padding: 0; box-sizing: border-box; }
  html, body { width: 999px; height: 1200px; overflow: hidden; }
  body {
    position: relative;
    background: var(--stage);
    font-family: "Arimo", Arial, sans-serif;
  }

  /* ---------- Front side ---------- */
  .card-front {
    position: absolute;
    left: 57px; top: 85px;
    width: 426px; height: 904px;
    background: var(--navy);
    overflow: hidden;
  }
  .card-front .art { position: absolute; inset: 0; }
  .brand {
    position: absolute; left: 40px; top: 25px;
    display: flex; align-items: center;
  }
  .brand-circle {
    width: 110px; height: 110px; border-radius: 50%;
    border: 7px solid var(--white);
  }
  .brand-divider {
    width: 2px; height: 100px; background: var(--white);
    margin: 0 14px 0 10px;
  }
  .brand-name {
    color: var(--white); font-weight: 700;
    text-transform: uppercase; line-height: 1.05;
  }
  .brand-name .line-1 { display: block; font-size: 25px; }
  .brand-name .line-2 { display: block; font-size: 17px; letter-spacing: 3.4px; margin-top: 4px; }

  .tagline {
    position: absolute; left: 0; right: 0; top: 144px;
    text-align: center; color: var(--white);
    font-family: "Oswald", "Arial Narrow", sans-serif;
    font-weight: 600; font-size: 29px; line-height: 37px;
  }

  .programs {
    position: absolute; left: 45px; top: 620px; right: 20px;
    color: var(--white);
  }
  .programs h2 { font-size: 23px; font-weight: 700; line-height: 27px; margin-bottom: 8px; }
  .programs ul { list-style: none; }
  .programs li {
    position: relative; padding-left: 21px;
    font-size: 17px; line-height: 24.5px;
  }
  .programs li::before {
    content: ""; position: absolute; left: 2px; top: 9px;
    width: 7px; height: 7px; border-radius: 50%; background: var(--white);
  }
  .phone-band {
    position: absolute; left: 0; right: 0; top: 812px; height: 44px;
    background: var(--white); color: var(--navy-deep);
    text-align: center; font-weight: 700; font-size: 41px; line-height: 44px;
    letter-spacing: 1px;
  }
  .web-address {
    position: absolute; left: 0; right: 0; top: 864px;
    text-align: center; color: var(--white); font-size: 18px;
  }

  /* ---------- Back side ---------- */
  .card-back {
    position: absolute;
    left: 524px; top: 87px;
    width: 425px; height: 902px;
    background: var(--white);
    border-top: 20px solid var(--navy);
  }
  .program-list { padding: 8px 25px 0 26px; }
  .program + .program { margin-top: 9px; }
  .program h3 {
    color: var(--navy); font-size: 16.5px; font-weight: 700;
    line-height: 21px; text-transform: uppercase;
  }
  .program h3 .sub { text-transform: none; }
  .program p {
    color: var(--ink); font-size: 13.3px; line-height: 19.3px;
    text-align: justify;
  }
  .program p.last { text-align: left; }
  .back-footer {
    position: absolute; left: 0; right: 0; bottom: 0; height: 54px;
    background: var(--navy); color: var(--white);
    text-align: center; font-size: 13.3px; line-height: 18px; padding-top: 8px;
  }
</style>
</head>
<body>

  <section class="card-front" aria-label="Flyer front">
    <svg class="art" width="426" height="904" viewBox="0 0 426 904" aria-hidden="false">
      <defs>
        <linearGradient id="board" x1="0" y1="0" x2="0" y2="1">
          <stop offset="0" stop-color="var(--board-dark)"/>
          <stop offset="0.6" stop-color="var(--board-mid)"/>
          <stop offset="1" stop-color="var(--board-dark)"/>
        </linearGradient>
      </defs>
      <rect x="0" y="200" width="426" height="370" fill="url(#board)" role="img"
            aria-label="Chalkboard photo with the words New Mindset New Results and a glowing light bulb"/>
      <path d="M0,0 H426 V205 C330,210 150,250 0,300 Z" fill="var(--navy)"/>
      <path d="M0,300 C150,250 330,210 426,205 V222 C330,226 150,268 0,318 Z" fill="var(--white)"/>
      <path d="M0,318 C150,268 330,226 426,222 V270 C320,266 160,290 0,328 Z" fill="var(--grey)"/>
      <path d="M0,538 C140,520 300,498 426,490 V540 C320,548 140,580 0,600 Z" fill="var(--grey)"/>
      <path d="M0,600 C140,580 320,548 426,540 V556 C320,562 140,594 0,616 Z" fill="var(--white)"/>
    </svg>

    <div class="brand">
      <span class="brand-circle" aria-hidden="true"></span>
      <span class="brand-divider" aria-hidden="true"></span>
      <span class="brand-name">
        <span class="line-1">Tranquil Harbour</span>
        <span class="line-2">Hypnotherapy</span>
      </span>
    </div>

    <p class="tagline">“There is nothing more<br>important than good health”</p>

    <div class="programs">
      <h2>Professional Hypnosis<br>Therapy Programs:</h2>
      <ul>
        <li>Weight Loss (Virtual Gastric Band)</li>
        <li>Sugar Addiction</li>
        <li>Quit Smoking</li>
        <li>Chronic Fatigue &amp; Chronic Pain Relief</li>
        <li>Stress Relief &amp; Deep Relaxation</li>
      </ul>
    </div>

    <div class="phone-band">1300 555 019</div>
    <p class="web-address">www.TranquilHarbourHypnotherapy.com.au</p>
  </section>

  <section class="card-back" aria-label="Flyer back">
    <div class="program-list">
      <article class="program">
        <h3>Weight Loss Program<br><span class="sub">(Virtual Gastric Band)</span></h3>
        <p>Achieve long term weight loss without dieting. Whether it’s losing 3kg or 30kg, we’ll help you become the shape and size you want to be.</p>
        <p>Our Internationally Accredited Program is proven to be 95% effective in clinical trials.</p>
        <p class="last">Number of Sessions: 6+</p>
      </article>

      <article class="program">
        <h3>Sugar Addiction Program</h3>
        <p>Excess sugar intake can lead to obesity, Type 2 Diabetes and tooth decay.</p>
        <p>The habit of reaching for soft drinks, chocolate, sweets, cakes and biscuits can be hard to break.</p>
        <p>By rewiring your subconscious habits, our Program puts you back in control.</p>
        <p class="last">Number of Sessions: 3+</p>
      </article>

      <article class="program">
        <h3>Quit Smoking Program</h3>
        <p>The facts speak for themselves. You are 10 times more likely to quit smoking for good using hypnotherapy.</p>
        <p>Expect to be a nonsmoker after completing the first session of our Program. (12 Month Guarantee)</p>
        <p class="last">Number of Sessions: 2</p>
      </article>

      <article class="program">
        <h3>Chronic Fatigue &amp; Chronic<br>Pain Relief Program</h3>
        <p>Chronic Fatigue, Fibromyalgia and Chronic Musculoskeletal Pain are diseases of modern living.</p>
        <p>The symptoms of fatigue and pain are very real, however the cause is usually emotional, and is generally hidden beyond our conscious awareness.</p>
        <p>Our Program comprises Education and Hypnosis to help you regain your health, your self esteem, your friends and your life, all in a manageable timeframe.</p>
        <p class="last">Number of Sessions: 6+</p>
      </article>

      <article class="program">
        <h3>Stress Relief &amp; Deep Relaxation<br>Program</h3>
        <p>Our Program gently uncovers the true source of your stress, and helps you reconnect to a natural inner calm. We teach you self hypnosis so that you have the tools to continue your experience.</p>
        <p class="last">Number of Sessions: 3+</p>
      </article>
    </div>

    <footer class="back-footer">
      All Programs include take home CD’s personally recorded<br>by our therapists, using advanced hypnotic techniques.
    </footer>
  </section>

</body>
</html>
```